Polystyrene Environmental Synopsis

We need a fact sheet for quick reference that groups information units and has a simple but engaging visual presentation of the text and various infographics. We are a trade association representing polystyrene foam manufacturers and this piece is intended to help our members provide effective messaging to their sales personnel.

To view our typical company design/style please see our website at www.kvrtradegroup.org. Our primary RGB colors are: (187,140,9); (94,47,29); (94,138,164); and (164,167,15). Secondary RGB colors are (249,162,28) and (218,210,208). Our title/header font is DIN Next LT Pro and our copy font is Calibri 10.5 pt. We can deviate from the font specification if beneficial.

Target Market(s)

Polystyrene manufacturer plant workers and other employees.

Font styles to use
Sans Serif

Requirements
Must have
• Information presentation must be clean and easy to reference.

```html
<!DOCTYPE html>
<html lang="en">
<head>
<meta charset="utf-8">
<title>EPS Recycling Fact Sheet</title>
<link href="https://fonts.googleapis.com/css2?family=Barlow+Condensed:wght@500;600;700;800&family=Carlito:ital,wght@0,400;0,700;1,700&display=swap" rel="stylesheet">
<style>
  :root{
    --brown:#5e2f1d;
    --gold:#bb8c09;
    --blue:#5e8aa4;
    --link-blue:#3d7fc1;
    --olive:#a4a70f;
    --orange:#f9a21c;
    --warm-grey:#dad2d0;
    --ink:#231f20;
    --bar-blue:#5b86c5;
    --bar-orange:#f39a4c;
    --value-blue:#2b4d7c;
    --value-orange:#b5601e;
    --year-grey:#9b9b9b;
  }
  *{box-sizing:border-box;margin:0;padding:0}
  html,body{width:849px;height:1200px;overflow:hidden;background:#fff}
  body{position:relative;font-family:"Carlito","Calibri",sans-serif;color:var(--ink)}

  /* brand */
  .brand{position:absolute;left:14px;top:50px;display:flex;align-items:center;gap:12px}
  .brand-dot{width:112px;height:112px;border-radius:50%;background:var(--gold)}
  .brand-name{font-family:"Carlito",sans-serif;font-size:24px;line-height:1.05;color:var(--brown);font-weight:400;width:130px}

  /* header band */
  .title-band{position:absolute;left:294px;top:40px;width:555px;height:158px;background:var(--brown);display:flex;align-items:center}
  .title-icon{width:112px;height:104px;margin-left:18px;background:#fff;border-radius:14px;opacity:.95}
  .title-band h1{font-family:"Barlow Condensed",sans-serif;font-weight:800;font-size:84px;color:#fff;letter-spacing:1px;margin-left:22px;line-height:1}

  /* locations panel */
  .locations{position:absolute;left:35px;top:209px;width:227px;height:449px;background:var(--olive);padding:10px 14px}
  .locations .count{font-family:"Barlow Condensed",sans-serif;font-weight:700;font-size:142px;line-height:112px;color:#fff;letter-spacing:2px;text-align:center}
  .locations .label{font-family:"Barlow Condensed",sans-serif;font-weight:600;font-size:21px;line-height:22px;letter-spacing:2px;color:var(--brown);margin-top:8px}
  .poster{position:absolute;left:15px;top:230px;width:183px;height:205px;background:linear-gradient(160deg,#38a6d8,#7cc8e8 55%,#2d6fa8);box-shadow:2px 3px 4px rgba(0,0,0,.35)}

  /* chart */
  .chart{position:absolute;left:35px;top:679px;width:227px;height:481px;border:4px solid var(--warm-grey);padding:12px 10px;overflow:hidden}
  .chart h3{font-family:"Barlow Condensed",sans-serif;font-weight:700;font-size:29px;color:var(--bar-orange);text-align:center;line-height:1}
  .chart .sub{font-family:"Barlow Condensed",sans-serif;font-weight:700;font-size:14px;color:var(--bar-blue);text-align:center;line-height:1.15;margin-top:4px}
  .chart .unit{font-family:"Barlow Condensed",sans-serif;font-weight:700;font-size:11px;letter-spacing:1.5px;color:var(--bar-blue);text-align:center}
  .rows{margin-top:8px}
  .row{position:relative;height:71px}
  .bar{position:absolute;left:34px;height:18px;font-size:13px;font-weight:700;line-height:18px}
  .bar span{position:absolute;left:calc(100% + 4px);white-space:nowrap}
  .bar.consumer{top:8px;background:var(--bar-blue)}
  .bar.industrial{top:30px;background:var(--bar-orange)}
  .bar.consumer span{color:var(--value-blue)}
  .bar.industrial span{color:var(--value-orange)}
  .icon{position:absolute;left:4px}
  .icon.person{top:6px}
  .icon.plant{top:32px}
  .year{position:absolute;right:2px;top:14px;font-family:"Barlow Condensed",sans-serif;font-weight:500;font-size:29px;line-height:1;color:var(--year-grey)}

  /* copy column */
  .copy{position:absolute;left:293px;top:214px;width:521px;font-size:11.4px;line-height:1.3;text-align:justify}
  .copy h2{font-family:"Carlito",sans-serif;font-weight:700;font-size:21px;color:var(--brown);text-align:left}
  .copy h4{font-family:"Carlito",sans-serif;font-weight:700;font-size:17px;color:var(--brown);margin:10px 0 2px;text-align:left}
  .copy p{margin-bottom:11px}
  .copy .lead{color:var(--link-blue);font-weight:700;font-style:italic}

  /* fact boxes */
  .fact-word{position:absolute;left:312px;top:636px;font-family:"Barlow Condensed",sans-serif;font-weight:800;font-size:56px;line-height:1;color:var(--ink);letter-spacing:1px}
  .box{position:absolute;left:293px;width:521px;background:var(--brown);color:#fff;border-top-left-radius:22px;padding:10px 18px 10px 20px}
  .box ul{list-style:none;font-size:12px;line-height:1.28}
  .box li{position:relative;padding-left:10px;margin-bottom:1px}
  .box li::before{content:"•";position:absolute;left:0}
  .box-recyclable{top:669px;min-height:184px}
  .box-recyclable h3{font-size:37px;font-weight:700;line-height:1;margin-bottom:8px}
  .box-recyclable h3 small{font-size:26px}
  .box-tech{top:884px;height:114px}
  .box-tech h3{font-size:29px;font-weight:700;line-height:1;margin-bottom:8px}
  .box-tech h3 em{font-style:normal;color:var(--orange);font-size:22px;font-weight:600}
  .box-markets{top:1008px;height:161px;padding-top:6px}
  .box-markets h3{font-weight:600;line-height:1;color:var(--orange);font-size:24px}
  .box-markets h3 strong{display:block;color:#fff;font-size:35px;font-weight:700;margin-left:158px;margin-top:-2px;margin-bottom:6px}
  .markets{display:grid;grid-template-columns:160px 220px;font-size:12px;margin-left:10px;margin-top:2px;row-gap:2px}
</style>
</head>
<body>

<div class="brand">
  <div class="brand-dot"></div>
  <div class="brand-name">KVR Trade Group</div>
</div>

<header class="title-band">
  <div class="title-icon" role="img" aria-label="Recycling symbol of three chasing arrows"></div>
  <h1>RECYCLING</h1>
</header>

<section class="locations">
  <div class="count">490</div>
  <div class="label">EPS RECYCLING<br>LOCATIONS IN<br>NORTH AMERICA</div>
  <div class="poster" role="img" aria-label="Cover of the blue 'Recycle your foam packaging here' poster showing accepted and rejected items"></div>
</section>

<section class="chart">
  <h3>EPS RECYCLING</h3>
  <div class="sub">POST-CONSUMER &amp; POST-INDUSTRIAL<br>2000-2016</div>
  <div class="unit">(MILLIONS OD POUNDS)</div>

  <div class="rows">
    <div class="row">
      <svg class="icon person" width="14" height="20" viewBox="0 0 14 20"><circle cx="7" cy="4" r="3.2" fill="#5b86c5"/><rect x="3" y="8" width="8" height="11" rx="2" fill="#5b86c5"/></svg>
      <svg class="icon plant" width="24" height="14" viewBox="0 0 24 14"><path d="M0 14V6l6 3V6l6 3V6l6 3V0h4v14z" fill="#f39a4c"/></svg>
      <div class="bar consumer" style="width:32px"><span>24.9</span></div>
      <div class="bar industrial" style="width:20px"><span>15.6</span></div>
      <div class="year">2000</div>
    </div>
    <div class="row">
      <svg class="icon person" width="14" height="20" viewBox="0 0 14 20"><circle cx="7" cy="4" r="3.2" fill="#5b86c5"/><rect x="3" y="8" width="8" height="11" rx="2" fill="#5b86c5"/></svg>
      <svg class="icon plant" width="24" height="14" viewBox="0 0 24 14"><path d="M0 14V6l6 3V6l6 3V6l6 3V0h4v14z" fill="#f39a4c"/></svg>
      <div class="bar consumer" style="width:33px"><span>25</span></div>
      <div class="bar industrial" style="width:43px"><span>32.9</span></div>
      <div class="year">2004</div>
    </div>
    <div class="row">
      <svg class="icon person" width="14" height="20" viewBox="0 0 14 20"><circle cx="7" cy="4" r="3.2" fill="#5b86c5"/><rect x="3" y="8" width="8" height="11" rx="2" fill="#5b86c5"/></svg>
      <svg class="icon plant" width="24" height="14" viewBox="0 0 24 14"><path d="M0 14V6l6 3V6l6 3V6l6 3V0h4v14z" fill="#f39a4c"/></svg>
      <div class="bar consumer" style="width:44px"><span>33.6</span></div>
      <div class="bar industrial" style="width:47px"><span>35.8</span></div>
      <div class="year">2008</div>
    </div>
    <div class="row">
      <svg class="icon person" width="14" height="20" viewBox="0 0 14 20"><circle cx="7" cy="4" r="3.2" fill="#5b86c5"/><rect x="3" y="8" width="8" height="11" rx="2" fill="#5b86c5"/></svg>
      <svg class="icon plant" width="24" height="14" viewBox="0 0 24 14"><path d="M0 14V6l6 3V6l6 3V6l6 3V0h4v14z" fill="#f39a4c"/></svg>
      <div class="bar consumer" style="width:48px"><span>36.7</span></div>
      <div class="bar industrial" style="width:20px"><span>15.6</span></div>
      <div class="year">2012</div>
    </div>
    <div class="row">
      <svg class="icon person" width="14" height="20" viewBox="0 0 14 20"><circle cx="7" cy="4" r="3.2" fill="#5b86c5"/><rect x="3" y="8" width="8" height="11" rx="2" fill="#5b86c5"/></svg>
      <svg class="icon plant" width="24" height="14" viewBox="0 0 24 14"><path d="M0 14V6l6 3V6l6 3V6l6 3V0h4v14z" fill="#f39a4c"/></svg>
      <div class="bar consumer" style="width:82px"><span>63</span></div>
      <div class="bar industrial" style="width:72px"><span>55.7</span></div>
      <div class="year">2016</div>
    </div>
  </div>
</section>

<article class="copy">
  <h2>EPS Talking Points</h2>
  <p>Polystyrene bans, recycling, and human health are top objections facing the EPS industry. When confronted with false allegations about EPS, here are some fast facts to help respond proactively. Perfect for packaging conferences, social media, and sales objectives.</p>
  <h4>Polystyrene Defense Line</h4>
  <p><span class="lead">Making Your Point</span>—Speaking with confidence means knowing your material. When responding to misstatements be prepared to challenge the source with factual information. Using a question format is less confrontational, e.g., “Did you know…” or “Were you aware…”? Make affirmative statements whenever possible; avoid restating the misinformation in your response. When addressing someone that refuses to give reasonable consideration to new information, we recommend responding, “It’s unfortunate you’re not willing to look into this further.”</p>
  <p>When given the opportunity to address an individual or an audience about EPS sustainability, focus on three (3) specific talking points to keep the discussion or presentation focused. Plan your talking points and don’t deviate; this is an effective strategy for dealing with media inquiries as well.</p>
  <p><span class="lead">Have a Bigger Voice</span>—The more educated we are, the more educated others will be. Share this document with your employees even if they do not deal directly with your customers or specific packaging audiences. Everyone working within the EPS industry should be aware of the strong environmental profile for EPS.</p>
</article>

<div class="fact-word">FACT</div>

<section class="box box-recyclable">
  <h3><small>EPS is </small>Recyclable</h3>
  <ul>
    <li>Historically, EPS recycling averages ~18% over a 25-year trendline.</li>
    <li>EPS recycling is most successful in commercial waste streams with large volume sources of EPS waste.</li>
    <li>Consumer access to EPS recycling sometimes requires extra effort, but with proper equipment &amp; handling, it is successful in many communities.</li>
    <li>Creative problem solving for challenging recycling scenarios means Northgate Mart, VitaPlan Foods, Harlow &amp; Pine Kitchen, Brightwell Appliances, Voltline Electronics, Prairie Cut Meats are committed to long term EPS recycling.</li>
  </ul>
</section>

<section class="box box-tech">
  <h3><em>New EPS Recycling Technologies</em> Are Emerging</h3>
  <ul>
    <li>Pyrolisis—a chemical reprocessing method—increases the ability to recycle contaminated EPS waste.</li>
    <li>Two new facilities opened in 2018</li>
  </ul>
</section>

<section class="box box-markets">
  <h3>EPS End-Markets Show <strong>Consistent Growth</strong></h3>
  <ul>
    <li>It is used as recycled content in new EPS packaging and other EPS products.</li>
    <li>Markets for recycled content EPS include:</li>
  </ul>
  <div class="markets">
    <span>— Crown Molding</span><span>— Picture Frames</span>
    <span>— Surfboards</span><span>— Other Rigid Polystyrene Applications</span>
  </div>
</section>

</body>
</html>
```